Simple+Professional tech feel + warm and friendly box design for pet test kit

Project Name: 10-Minute Canine & Feline Rapid Test Kit Packaging Design
Target Brand Reference: VETRALUX (South Korea) styles
Design Style Direction: Professional tech feel + warm and friendly
Professionalism (Professional): Clear typography and distinct information hierarchy to reflect the product’s scientific rigor and accuracy.
Technological: Reflected through clean graphics and a minimalist layout.
Friendly: Utilise soft, warm colour combinations to convey care for pets and well-wishes for their health.
International: The design should align with mainstream aesthetics and avoid cultural ambiguities.

Target Market(s)
European Union and the United States
Industry/Entity Type
Veterinary Medical
Look and feel
Each slider illustrates characteristics of the customer's brand and the style your logo design should communicate.

```html
<!DOCTYPE html>
<html lang="en">
<head>
<meta charset="utf-8">
<title>Petlumo Rapid Test Kit Packaging</title>
<link href="https://fonts.googleapis.com/css2?family=Mulish:wght@400;700;800;900&display=swap" rel="stylesheet">
<style>
  :root{
    --stage:#e6e6e6;
    --brand-blue:#1190c9;
    --deep-blue:#0f7cc2;
    --leaf-green:#8cc63f;
    --light-green:#9ccf4a;
    --paper:#ffffff;
    --ink:#1d2a2a;
    --mist:#e3ebf5;
  }
  *{box-sizing:border-box;margin:0;padding:0}
  html,body{width:1200px;height:800px;overflow:hidden}
  body{background:var(--stage);font-family:"Mulish",sans-serif;position:relative}

  .panel{position:absolute;overflow:hidden}

  /* top lid */
  .lid{left:380px;top:60px;width:640px;height:260px;background:var(--brand-blue)}
  .lid-mark{position:absolute;left:0;right:0;top:70px;text-align:center;transform:rotate(180deg);
    color:var(--paper);font-weight:900;font-size:110px;letter-spacing:-1px;line-height:1}
  .lid-mark sup{font-size:18px;font-weight:400;vertical-align:top;margin-left:4px}

  /* front */
  .front{left:380px;top:320px;width:640px;height:400px;background:var(--paper)}
  .front-texture{position:absolute;inset:0;
    background:radial-gradient(ellipse at 85% 20%,var(--mist) 0%,rgba(255,255,255,0) 55%),
               radial-gradient(ellipse at 15% 70%,var(--mist) 0%,rgba(255,255,255,0) 45%)}
  .count-tab{position:absolute;left:0;top:40px;height:50px;width:250px;background:var(--light-green);
    clip-path:polygon(0 0,100% 0,88% 100%,0 100%);color:var(--paper);font-weight:700;font-size:26px;
    padding:8px 0 0 26px}
  .front-mark{position:absolute;left:40px;top:128px;color:var(--deep-blue);font-weight:900;font-size:96px;
    line-height:1;letter-spacing:-1px;white-space:nowrap}
  .front-mark sup{font-size:18px;font-weight:400;vertical-align:top;margin-left:4px}
  .pet-art{position:absolute;right:30px;top:70px;width:150px;height:170px;border-radius:10px;
    background:linear-gradient(160deg,#d6ecf8,#eaf4fb)}
  .product-title{position:absolute;left:24px;top:270px;color:var(--ink)}
  .product-title h1{font-size:22px;font-weight:800;line-height:1.2}
  .product-title p{font-size:18px;font-weight:400;margin-top:2px}
  .maker-band{position:absolute;left:0;right:0;bottom:0;height:46px;
    background:linear-gradient(90deg,var(--light-green) 0%,#c9e69e 45%,rgba(255,255,255,0) 80%);
    border-top:4px solid var(--deep-blue)}
  .maker-name{position:absolute;left:24px;top:8px;font-weight:800;font-size:22px;color:var(--ink)}

  /* side */
  .side{left:120px;top:320px;width:260px;height:400px;background:var(--leaf-green);color:var(--paper);text-align:center}
  .side-mark{margin-top:38px;font-weight:900;font-size:44px;line-height:1}
  .side-mark sup{font-size:10px;font-weight:400;vertical-align:top}
  .side-note{margin:18px auto 0;width:220px;font-weight:800;font-size:15px;line-height:1.35}
  .side-info{margin:22px auto 0;width:220px;font-size:12px;line-height:1.5}
  .side-info strong{font-weight:800;font-size:13px}
  .symbols{position:absolute;left:18px;right:18px;bottom:26px;display:flex;align-items:center;justify-content:space-between;color:var(--ink)}
  .ivd{border:1.5px solid var(--ink);font-size:12px;padding:2px 5px;font-weight:700}
  .temp{font-size:11px;font-weight:700;display:flex;align-items:center;gap:2px}
</style>
</head>
<body>

<section class="panel lid">
  <div class="lid-mark">Petlumo<sup>TM</sup></div>
</section>

<section class="panel side">
  <div class="side-mark">Petlumo<sup>TM</sup></div>
  <p class="side-note">(For Accurate Results, Please Read The Instructions Carefully Before Use)</p>
  <p class="side-info">A Clear View into Pet Health<br><strong>Made by Norvane</strong><br>Norvane Biotech Limited<br>Web:www.norvane.com<br>E-mail:sales@norvane.com</p>
  <div class="symbols">
    <svg width="24" height="24" viewBox="0 0 24 24" aria-label="Do not reuse"><circle cx="12" cy="12" r="10" fill="none" stroke="#1d2a2a" stroke-width="2"/><text x="12" y="17" text-anchor="middle" font-size="14" font-weight="800" fill="#1d2a2a" font-family="Mulish,sans-serif">2</text><line x1="5" y1="19" x2="19" y2="5" stroke="#1d2a2a" stroke-width="1.5"/></svg>
    <svg width="24" height="24" viewBox="0 0 24 24" aria-label="Keep dry"><path d="M2 12a10 8 0 0 1 20 0z" fill="#1d2a2a"/><path d="M12 12v7a2 2 0 0 1-4 0" fill="none" stroke="#1d2a2a" stroke-width="2"/></svg>
    <svg width="24" height="24" viewBox="0 0 24 24" aria-label="Keep away from sunlight"><circle cx="12" cy="12" r="5" fill="none" stroke="#1d2a2a" stroke-width="2"/><g stroke="#1d2a2a" stroke-width="2"><line x1="12" y1="1" x2="12" y2="4"/><line x1="12" y1="20" x2="12" y2="23"/><line x1="1" y1="12" x2="4" y2="12"/><line x1="20" y1="12" x2="23" y2="12"/><line x1="3" y1="21" x2="21" y2="3"/></g></svg>
    <span class="ivd">IVD</span>
    <span class="temp">4°C<svg width="8" height="22" viewBox="0 0 8 22"><line x1="4" y1="1" x2="4" y2="16" stroke="#1d2a2a" stroke-width="1.5"/><circle cx="4" cy="18" r="3" fill="#1d2a2a"/></svg>30°C</span>
  </div>
</section>

<section class="panel front">
  <div class="front-texture"></div>
  <div class="count-tab">5 Tests/Kit</div>
  <div class="front-mark">Petlumo<sup>TM</sup></div>
  <div class="pet-art" role="img" aria-label="Blue line illustration of a dog and a cat in profile"></div>
  <div class="product-title">
    <h1>10-Minute Canine &amp;<br>Feline Rapid Test Kit</h1>
    <p>For Dogs and Cats</p>
  </div>
  <div class="maker-band"><span class="maker-name">Norvane</span></div>
</section>

</body>
</html>
```